Cover of the e-book award-winning national sports figure.

I would like to utilize the picture this attached to this brief. If you could pull the trophies and myself out and place with the new background, that’s what I would like to see . I would like to have a new bookcover design for my e-book. I attached below the original cover and have marked in red. The things that I don’t want on the new cover. I’ve attached a picture that’s not the original. I’m waiting on the high copy. I would like to replace the old logo with the one that I have attached. The website that I would like to have on the book is www.dellanvmoreaux.com.
Target Market(s)
Biography
Industry/Entity Type
Sports & motivation?
Requirements
Must have
- Picture of me in the blue suit on the cover the title of the book walking past midnight lessons from quiet harbors
Nice to have
- Utilize the old cover that I have attached for some ideas
Should not have
- The cover should not have anything related to marlow crest press Inc.

```html
<!DOCTYPE html>
<html lang="en">
<head>
<meta charset="utf-8">
<title>Walking Past Midnight — Dellan V. Moreaux</title>
<link href="https://fonts.googleapis.com/css2?family=Lato:ital,wght@0,400;0,700;0,900;1,400&family=Oswald:wght@400;500&family=Playfair+Display:wght@500;600&display=swap" rel="stylesheet">
<style>
  :root {
    --navy: #1b2a52;
    --slate: #5f6a75;
    --mist: #e8eef5;
    --ice: #c9ddef;
    --sky: #7aaad4;
    --body-text: #d3dfeb;
    --white: #ffffff;
  }
  * { margin: 0; padding: 0; box-sizing: border-box; }
  html, body { width: 750px; height: 1200px; overflow: hidden; background: var(--mist); }
  .cover { position: relative; width: 750px; height: 1200px; background: var(--mist); overflow: hidden; font-family: "Lato", sans-serif; }
  .slate-panel { position: absolute; left: 0; top: 0; width: 664px; height: 960px; background: var(--slate); box-shadow: 4px 6px 10px rgba(0,0,0,.18); }
  .author-band { position: absolute; left: 102px; top: 0; width: 648px; height: 94px; background: var(--navy); box-shadow: 0 4px 8px rgba(0,0,0,.25); display: flex; align-items: center; justify-content: center; z-index: 4; }
  .author-band h2 { font-family: "Lato", sans-serif; font-weight: 700; font-size: 56px; color: var(--ice); letter-spacing: .5px; }
  .portrait { position: absolute; left: 462px; top: 180px; width: 288px; height: 1020px; border-radius: 130px 130px 0 0; background: linear-gradient(180deg, #b07a5a 0%, #a06a4c 22%, #dde6f2 26%, #2f4f9a 34%, #24417f 100%); z-index: 2; }
  .trophies { position: absolute; left: 215px; top: 695px; width: 265px; height: 505px; background: linear-gradient(180deg, #d8dde3 0%, #9aa1aa 45%, #6f757c 80%, #3b2420 90%, #2e1b18 100%); border-radius: 110px 110px 0 0; z-index: 1; }
  .title { position: absolute; left: 0; top: 0; z-index: 3; color: var(--ice); }
  .title .big { position: absolute; font-family: "Playfair Display", serif; font-weight: 600; color: var(--ice); white-space: nowrap; line-height: 1; }
  .title .w1 { left: 92px; top: 118px; font-size: 132px; }
  .title .w3 { left: 196px; top: 268px; font-size: 122px; }
  .title .small { position: absolute; left: 96px; top: 330px; font-family: "Oswald", sans-serif; font-weight: 500; font-size: 58px; color: var(--ice); line-height: 1; }
  .title svg { position: absolute; left: 94px; top: 394px; }
  .subtitle-band { position: absolute; left: 0; top: 435px; width: 445px; height: 51px; background: var(--sky); box-shadow: 3px 4px 6px rgba(0,0,0,.2); display: flex; align-items: center; padding-left: 42px; z-index: 3; }
  .subtitle-band p { font-style: italic; font-size: 30px; color: var(--navy); white-space: nowrap; }
  .foreword { position: absolute; left: 100px; width: 345px; top: 492px; text-align: right; font-family: "Oswald", sans-serif; color: var(--white); z-index: 3; white-space: nowrap; }
  .foreword .lead { font-size: 27px; }
  .foreword .name { font-size: 42px; }
  .blurb { position: absolute; left: 46px; font-style: italic; font-size: 14.5px; line-height: 19.6px; color: var(--body-text); z-index: 3; }
  .blurb.first { top: 572px; width: 410px; }
  .blurb.second { top: 708px; width: 172px; }
  .imprint { position: absolute; left: 52px; top: 1020px; display: flex; align-items: center; gap: 10px; z-index: 3; }
  .imprint .dot { width: 22px; height: 22px; border-radius: 50%; background: #1f7fd1; }
  .imprint span { font-family: "Lato", sans-serif; font-weight: 900; font-size: 14px; color: #1a1a1a; letter-spacing: .5px; }
  .url-band { position: absolute; left: 0; top: 1122px; width: 290px; height: 55px; background: var(--slate); display: flex; align-items: center; padding-left: 46px; z-index: 0; }
  .url-band p { font-family: "Oswald", sans-serif; font-size: 21px; color: var(--white); }
</style>
</head>
<body>
<main class="cover">
  <div class="slate-panel"></div>
  <div class="url-band"><p>dellanvmoreaux.com</p></div>

  <header class="author-band"><h2>Dellan V. Moreaux</h2></header>

  <div class="trophies" role="img" aria-label="Photo of two silver championship trophies on a dark wooden stand"></div>
  <div class="portrait" role="img" aria-label="Photo of the author smiling in a blue pinstripe suit and paisley tie"></div>

  <h1 class="title">
    <span class="big w1">Walking</span>
    <span class="small">PAST</span>
    <svg width="178" height="20" viewBox="0 0 178 20" aria-hidden="true"><path d="M2 8 Q90 2 176 5 L170 10 Q140 14 110 18 Q125 12 130 11 Q60 12 4 12 Z" fill="#e8eef5"/></svg>
    <span class="big w3">Midnight</span>
  </h1>

  <div class="subtitle-band"><p>Lessons from Quiet Harbors</p></div>
  <p class="foreword"><span class="lead">Foreward by </span><span class="name">Corwin Blake</span></p>

  <p class="blurb first">Becoming a team player is absolutely crucial to your ultimate success. Learning to play within the framework of a team atmosphere not only strengthens your individual ability, but it also gives you a tremendous feeling of accomplishment knowing that you’ve been instrumental in moving an entire group of people a little closer to the collective dream.</p>
  <p class="blurb second">I believe that the personal and professional experiences shared in this book will offer strategies that can be used in any team situation, whether it’s a corporate sales force, a little league sports team, a social organization or a family unit.</p>

  <div class="imprint"><div class="dot"></div><span>DELLAN V. MOREAUX</span></div>
</main>
</body>
</html>
```